Football field themed poster-game

I'm looking for a 22" x 29" size poster with a minimum of 300dpi, max of 300mb. File format can be jpg, gif, tiff or bmp. Would like the field portion of the poster to appear like a real grass football field. The field will need makers for each yard. I've added an addition simple clip art that shows another way for yard lines as well.The rest of the layout I would like similar, but made to look more professional. Wording should be the same as in the given draft and located in the same area or close to that area on the poster. The style is open, but should be a little minimalist in nature. Design work has to be original and cannot be taken from trademarked or copyrighted items.
Updates

Project Deadline Extended
Reason: I have 2 or 3 designs that really standout, but I would like to see just a few more.

Target Market(s)

Football fans

Font styles to use
Sans Serif

Colors

Designer to choose colors to be used in the design.

Requirements
Must have
• The design must have the same similar layout as the file I have submitted with the contest. The football field needs to be made to look like a real field with turf. boarders would be nice and a modern look.
Should not have
• hard to read fonts, changes to the major overall layout of poster.

```html
<!DOCTYPE html>
<html lang="en">
<head>
<meta charset="utf-8">
<title>Tap Bowl – Football Field Poster Game</title>
<link href="https://fonts.googleapis.com/css2?family=Alfa+Slab+One&family=Montserrat:wght@800&display=swap" rel="stylesheet">
<style>
  :root {
    --paper: #ffffff;
    --turf: #5e9a2a;
    --turf-light: #72ad35;
    --turf-dark: #4c8520;
    --chalk: #f4f6ee;
    --cream: #f1ecc9;
    --visitors: #e1441c;
    --home: #2440a2;
    --score-red: #d9331f;
    --score-blue: #1f3ea6;
  }
  * { margin: 0; padding: 0; box-sizing: border-box; }
  html, body { width: 910px; height: 1200px; overflow: hidden; background: var(--paper); }
  .poster { position: relative; width: 910px; height: 1200px; background: var(--paper); }
  .score-dial { position: absolute; left: 18px; width: 340px; height: 340px; }
  .score-dial--visitors { top: 18px; }
  .score-dial--home { top: 854px; }
  .score-label { font-family: "Montserrat", sans-serif; font-weight: 800; font-size: 30px; letter-spacing: 1px; }
  .event-panel { position: absolute; left: 10px; top: 378px; width: 356px; height: 444px; }
  .event-mark__name { font-family: "Alfa Slab One", serif; font-size: 54px; fill: var(--cream); letter-spacing: 4px; }
  .field { position: absolute; left: 377px; top: 10px; width: 522px; height: 1180px; }
  .band-label { font-family: "Alfa Slab One", serif; font-size: 62px; fill: var(--chalk); }
  .yard-number { font-family: "Alfa Slab One", serif; font-size: 34px; fill: var(--chalk); }
</style>
</head>
<body>
<main class="poster">

  <svg width="0" height="0" style="position:absolute" aria-hidden="true">
    <defs>
      <filter id="turfGrain" x="0" y="0" width="100%" height="100%">
        <feTurbulence type="fractalNoise" baseFrequency="0.95 0.55" numOctaves="3" seed="7" result="noise"/>
        <feColorMatrix in="noise" values="0 0 0 0 0.12  0 0 0 0 0.28  0 0 0 0 0.04  0 0 0 -2.2 1.35" result="dark"/>
        <feTurbulence type="fractalNoise" baseFrequency="1.1 0.7" numOctaves="2" seed="19" result="noise2"/>
        <feColorMatrix in="noise2" values="0 0 0 0 0.62  0 0 0 0 0.82  0 0 0 0 0.35  0 0 0 2.4 -1.25" result="light"/>
        <feMerge><feMergeNode in="dark"/><feMergeNode in="light"/></feMerge>
      </filter>
      <linearGradient id="turfShade" x1="0" y1="0" x2="1" y2="1">
        <stop offset="0" stop-color="var(--turf-light)"/>
        <stop offset="0.5" stop-color="var(--turf)"/>
        <stop offset="1" stop-color="var(--turf-dark)"/>
      </linearGradient>
    </defs>
  </svg>

  <svg class="score-dial score-dial--visitors" viewBox="0 0 340 340" aria-label="Visitors score">
    <defs><path id="visitorsArc" d="M 50 210 A 132 132 0 0 0 176 314"/></defs>
    <circle cx="170" cy="170" r="112" fill="none" stroke="var(--score-red)" stroke-width="2"/>
    <path d="M 98 46 A 142 142 0 0 1 306 128" fill="none" stroke="var(--score-red)" stroke-width="1.5"/>
    <path d="M 56 86 A 152 152 0 0 1 322 196" fill="none" stroke="var(--score-red)" stroke-width="1"/>
    <path d="M 302 232 A 144 144 0 0 1 216 306" fill="none" stroke="var(--score-red)" stroke-width="4"/>
    <path d="M 310 250 A 160 160 0 0 1 130 326" fill="none" stroke="var(--score-red)" stroke-width="1.5"/>
    <path d="M 14 206 A 160 160 0 0 0 84 300" fill="none" stroke="var(--score-red)" stroke-width="3"/>
    <text class="score-label" fill="var(--score-red)"><textPath href="#visitorsArc">SCORE</textPath></text>
  </svg>

  <svg class="event-panel" viewBox="0 0 356 444" aria-label="Tap Bowl event panel">
    <rect width="356" height="444" fill="url(#turfShade)"/>
    <rect width="356" height="444" filter="url(#turfGrain)" opacity="0.6"/>
    <g transform="translate(178 222) rotate(90)">
      <circle cx="-190" cy="0" r="12" fill="var(--cream)"/>
      <text class="event-mark__name" x="14" y="0" text-anchor="middle" dominant-baseline="central">TAP BOWL</text>
    </g>
  </svg>

  <svg class="score-dial score-dial--home" viewBox="0 0 340 340" aria-label="Home score">
    <defs><path id="homeArc" d="M 62 170 A 116 116 0 0 1 176 54"/></defs>
    <circle cx="170" cy="170" r="112" fill="none" stroke="var(--score-blue)" stroke-width="2"/>
    <path d="M 30 120 A 146 146 0 0 1 130 30" fill="none" stroke="var(--score-blue)" stroke-width="1.5"/>
    <path d="M 18 184 A 152 152 0 0 1 90 40" fill="none" stroke="var(--score-blue)" stroke-width="3"/>
    <path d="M 294 106 A 144 144 0 0 1 224 304" fill="none" stroke="var(--score-blue)" stroke-width="1.5"/>
    <path d="M 318 126 A 158 158 0 0 1 112 318" fill="none" stroke="var(--score-blue)" stroke-width="1"/>
    <path d="M 40 228 A 144 144 0 0 0 124 306" fill="none" stroke="var(--score-blue)" stroke-width="4"/>
    <text class="score-label" fill="var(--score-blue)"><textPath href="#homeArc">SCORE</textPath></text>
  </svg>

  <svg class="field" viewBox="0 0 522 1180" aria-label="Football field">
    <defs>
      <pattern id="yardTicks" x="0" y="96" width="14" height="9.86" patternUnits="userSpaceOnUse">
        <rect x="0" y="4" width="14" height="2" fill="var(--chalk)"/>
      </pattern>
      <pattern id="sideTicks" x="0" y="96" width="8" height="9.86" patternUnits="userSpaceOnUse">
        <rect x="0" y="4" width="8" height="2" fill="var(--chalk)"/>
      </pattern>
    </defs>

    <rect class="end-zone end-zone--visitors" x="0" y="0" width="522" height="94" fill="var(--visitors)"/>
    <rect class="turf" x="0" y="96" width="522" height="986" fill="url(#turfShade)"/>
    <rect class="end-zone end-zone--home" x="0" y="1084" width="522" height="96" fill="var(--home)"/>

    <g class="mow-stripes" fill="#ffffff" opacity="0.06">
      <rect x="0" y="145.3" width="522" height="49.3"/>
      <rect x="0" y="243.9" width="522" height="49.3"/>
      <rect x="0" y="342.5" width="522" height="49.3"/>
      <rect x="0" y="441.1" width="522" height="49.3"/>
      <rect x="0" y="539.7" width="522" height="49.3"/>
      <rect x="0" y="638.3" width="522" height="49.3"/>
      <rect x="0" y="736.9" width="522" height="49.3"/>
      <rect x="0" y="835.5" width="522" height="49.3"/>
      <rect x="0" y="934.1" width="522" height="49.3"/>
      <rect x="0" y="1032.7" width="522" height="49.3"/>
    </g>

    <rect class="turf-grain" x="0" y="0" width="522" height="1180" filter="url(#turfGrain)" opacity="0.6"/>

    <text class="band-label" transform="translate(261 48) rotate(180)" text-anchor="middle" dominant-baseline="central" textLength="328" lengthAdjust="spacingAndGlyphs">VISITORS</text>
    <text class="band-label" x="261" y="1134" text-anchor="middle" dominant-baseline="central" textLength="206" lengthAdjust="spacingAndGlyphs">HOME</text>

    <g class="yard-lines" stroke="var(--chalk)" stroke-width="2.6">
      <line x1="0" x2="522" y1="96" y2="96"/>
      <line x1="0" x2="522" y1="145.3" y2="145.3"/>
      <line x1="0" x2="522" y1="194.6" y2="194.6"/>
      <line x1="0" x2="522" y1="243.9" y2="243.9"/>
      <line x1="0" x2="522" y1="293.2" y2="293.2"/>
      <line x1="0" x2="522" y1="342.5" y2="342.5"/>
      <line x1="0" x2="522" y1="391.8" y2="391.8"/>
      <line x1="0" x2="522" y1="441.1" y2="441.1"/>
      <line x1="0" x2="522" y1="490.4" y2="490.4"/>
      <line x1="0" x2="522" y1="539.7" y2="539.7"/>
      <line x1="0" x2="522" y1="589" y2="589"/>
      <line x1="0" x2="522" y1="638.3" y2="638.3"/>
      <line x1="0" x2="522" y1="687.6" y2="687.6"/>
      <line x1="0" x2="522" y1="736.9" y2="736.9"/>
      <line x1="0" x2="522" y1="786.2" y2="786.2"/>
      <line x1="0" x2="522" y1="835.5" y2="835.5"/>
      <line x1="0" x2="522" y1="884.8" y2="884.8"/>
      <line x1="0" x2="522" y1="934.1" y2="934.1"/>
      <line x1="0" x2="522" y1="983.4" y2="983.4"/>
      <line x1="0" x2="522" y1="1032.7" y2="1032.7"/>
      <line x1="0" x2="522" y1="1082" y2="1082"/>
    </g>

    <g class="hash-marks">
      <rect x="190" y="106" width="14" height="966" fill="url(#yardTicks)"/>
      <rect x="318" y="106" width="14" height="966" fill="url(#yardTicks)"/>
      <rect x="0" y="106" width="8" height="966" fill="url(#sideTicks)"/>
      <rect x="514" y="106" width="8" height="966" fill="url(#sideTicks)"/>
    </g>

    <g class="yard-numbers yard-numbers--left" text-anchor="middle" dominant-baseline="central">
      <text class="yard-number" transform="translate(90 194.6) rotate(90)">10</text>
      <text class="yard-number" transform="translate(90 293.2) rotate(90)">20</text>
      <text class="yard-number" transform="translate(90 391.8) rotate(90)">30</text>
      <text class="yard-number" transform="translate(90 490.4) rotate(90)">40</text>
      <text class="yard-number" transform="translate(90 589) rotate(90)">50</text>
      <text class="yard-number" transform="translate(90 687.6) rotate(90)">40</text>
      <text class="yard-number" transform="translate(90 786.2) rotate(90)">30</text>
      <text class="yard-number" transform="translate(90 884.8) rotate(90)">20</text>
      <text class="yard-number" transform="translate(90 983.4) rotate(90)">10</text>
    </g>
    <g class="yard-numbers yard-numbers--right" text-anchor="middle" dominant-baseline="central">
      <text class="yard-number" transform="translate(432 194.6) rotate(-90)">10</text>
      <text class="yard-number" transform="translate(432 293.2) rotate(-90)">20</text>
      <text class="yard-number" transform="translate(432 391.8) rotate(-90)">30</text>
      <text class="yard-number" transform="translate(432 490.4) rotate(-90)">40</text>
      <text class="yard-number" transform="translate(432 589) rotate(-90)">50</text>
      <text class="yard-number" transform="translate(432 687.6) rotate(-90)">40</text>
      <text class="yard-number" transform="translate(432 786.2) rotate(-90)">30</text>
      <text class="yard-number" transform="translate(432 884.8) rotate(-90)">20</text>
      <text class="yard-number" transform="translate(432 983.4) rotate(-90)">10</text>
    </g>

    <g class="yard-arrows" fill="var(--chalk)">
      <path d="M 86 171 L 94 171 L 90 164 Z"/><path d="M 428 171 L 436 171 L 432 164 Z"/>
      <path d="M 86 270 L 94 270 L 90 263 Z"/><path d="M 428 270 L 436 270 L 432 263 Z"/>
      <path d="M 86 368 L 94 368 L 90 361 Z"/><path d="M 428 368 L 436 368 L 432 361 Z"/>
      <path d="M 86 467 L 94 467 L 90 460 Z"/><path d="M 428 467 L 436 467 L 432 460 Z"/>
      <path d="M 86 711 L 94 711 L 90 718 Z"/><path d="M 428 711 L 436 711 L 432 718 Z"/>
      <path d="M 86 809 L 94 809 L 90 816 Z"/><path d="M 428 809 L 436 809 L 432 816 Z"/>
      <path d="M 86 908 L 94 908 L 90 915 Z"/><path d="M 428 908 L 436 908 L 432 915 Z"/>
      <path d="M 86 1007 L 94 1007 L 90 1014 Z"/><path d="M 428 1007 L 436 1007 L 432 1014 Z"/>
    </g>
  </svg>

</main>
</body>
</html>
```